Redesign of Plastic Surgeon Website to fully responsive / modern feel

Hi

Our current website is out of date www.harbourlinecosmetic.org

We want a fresh / modern looking design
Needs to be fully responsive design that works extremely well on ipad and mobile device

Would like design for both full screen website and mobile

Have listed a few websites of other plastic surgeons we like
http://www.reformclinicplus.com/
http://www.doriankeelermd.com/
http://www.tarrantcontours.com/
http://www.oakdenecosmeticsurgery.com/

Menu needs to include
1. About Us
2. Procedures (see current website for example)
3. News
4. Patient Resources
5. Contact Us

We are flexible with colours / images / layout

I have uploaded a document that has some content - the face pages content is completed only

some of the procedures can have content upwards of 4000 words - total website can be large with over 40,000 words
Updates

Hi I have updated the logo for our design for the new website - this is the logo and colours we want reflected throughout the siteThanks Added Wednesday, January 13, 2016

Target Market(s)

Mainly women 20-60 85% of practice
Some men 15%

Industry/Entity Type

Plastic Surgery

Number of Pages Required

5+ page

Requirements
Must have
• We need designs for
• Homepage
• Internal pages
• 1. Landing pages for breast / body / face / non surgical main pages
• 2. Procedure pages for individual pages under each section - eg breast augmentation
• 3. About us pages - like meet the doctor, our staff, clinics
• 4. Contact page
• 5. Blog / News page
Nice to have
• See our list of websites for examples of designs we like
• Like full screen design with nice hero image
• Needs to have good to call to action messages on home page like
• Specials, procedure of the month, etc

```html
<!DOCTYPE html>
<html lang="en">
<head>
<meta charset="utf-8">
<title>Harbourline Cosmetic Institute</title>
<link href="https://fonts.googleapis.com/css2?family=Raleway:wght@300;400;600&family=Open+Sans:wght@400;600;700&display=swap" rel="stylesheet">
<style>
:root{
  --accent:#29a9dc;
  --accent-dark:#1d8fbd;
  --ink:#333;
  --muted:#777;
  --light:#f3f3f3;
  --line:#dedede;
  --dark:#2e2e2e;
  --darker:#222;
  --card-dark:#3b3b3b;
  --white:#fff;
}
*{box-sizing:border-box;margin:0;padding:0}
html,body{width:1200px;height:3548px;overflow:hidden}
body{font-family:"Open Sans",Arial,sans-serif;color:var(--ink);background:var(--white);font-size:11px;line-height:1.55;position:relative}
.section{position:absolute;left:0;width:1200px}
.wrap{position:absolute;left:160px;width:880px;top:0;bottom:0}
h2.sec-title{font-family:"Raleway",Arial,sans-serif;font-weight:400;font-size:24px;color:var(--ink);position:relative;padding-bottom:10px}
h2.sec-title::after{content:"";position:absolute;left:0;bottom:0;width:44px;height:3px;background:var(--accent)}
.btn{display:inline-block;background:var(--accent);color:var(--white);font-size:11px;font-weight:600;padding:8px 18px;border-radius:2px;text-decoration:none}
.readmore{color:var(--accent);font-size:10px;font-weight:600}
.ph{display:block}

/* header */
.site-header{top:0;height:176px;border-bottom:1px solid var(--line)}
.brand{position:absolute;left:0;top:22px;display:flex;align-items:center;gap:10px}
.brand-mark{width:26px;height:26px;background:var(--accent)}
.brand-name{font-family:"Raleway",Arial,sans-serif;font-weight:600;font-size:15px;color:#555;line-height:1.2;width:170px;text-transform:uppercase;letter-spacing:1px}
.top-cta{position:absolute;right:0;top:14px;font-size:10px;padding:6px 14px}
.top-phone{position:absolute;right:0;top:46px;font-size:15px;color:#555;display:flex;align-items:center;gap:6px}
.socials{position:absolute;right:0;top:76px;display:flex;gap:5px}
.socials span{width:18px;height:18px;background:#555;display:block}
.nav{position:absolute;left:0;top:118px;display:flex;gap:28px;font-size:11px;font-weight:600;text-transform:uppercase;color:#555}
.nav .active{color:var(--ink);border-bottom:3px solid var(--accent);padding-bottom:12px}
.search{position:absolute;right:0;top:112px;width:150px;height:24px;border:1px solid var(--line);font-size:10px;color:#aaa;padding:4px 8px}
.search svg{position:absolute;right:6px;top:5px}

/* hero */
.hero{top:176px;height:352px;background:#e6e6e6}
.hero-side{position:absolute;top:0;height:352px;background:linear-gradient(90deg,#cfcfcf,#bdbdbd)}
.hero-main{position:absolute;left:160px;width:880px;top:0;height:352px;background:linear-gradient(90deg,#f4f4f4 0%,#dcdcdc 45%,#8a8a8a 75%,#5a5a5a 100%)}
.hero-copy{position:absolute;left:56px;top:80px;width:330px}
.hero-copy h1{font-family:"Raleway",Arial,sans-serif;font-weight:300;font-size:30px;line-height:1.25;color:var(--ink);margin-bottom:26px}
.hero-next{position:absolute;left:1044px;top:80px;font-family:"Raleway",Arial,sans-serif;font-size:30px;color:var(--accent);line-height:1.3}
.hero-next small{display:block;color:#fff;font-size:30px}

/* procedures */
.procedures{top:528px;height:482px}
.procedures h2{position:absolute;left:0;top:60px}
.proc-cards{position:absolute;left:16px;top:144px;display:flex;gap:55px}
.proc-card{width:188px;background:var(--card-dark);color:#ccc;text-align:center}
.proc-card .ph{width:188px;height:168px;background:linear-gradient(160deg,#e8e8e8,#9b9b9b)}
.proc-card h3{font-family:"Raleway",Arial,sans-serif;font-weight:400;font-size:18px;color:var(--white);margin:8px 0 4px}
.proc-card p{font-size:9px;line-height:1.4;padding:0 12px;color:#bbb}
.proc-card .readmore{display:block;padding:8px 0 12px;color:var(--white)}

/* institute */
.institute{top:1010px;height:200px}
.institute h2{font-family:"Raleway",Arial,sans-serif;font-size:18px;font-weight:400}
.institute .sub{font-size:10px;color:var(--muted);margin:2px 0 8px}
.institute p{font-size:9.5px;color:var(--muted);line-height:1.6}
.institute .center{text-align:center;margin-top:16px}

/* doctor */
.doctor{top:1210px;height:410px}
.doctor h2{position:absolute;left:0;top:16px}
.doc-box{position:absolute;left:0;top:62px;width:880px;height:320px;border:1px solid var(--line);background:var(--white)}
.doc-photo{position:absolute;left:28px;top:20px;width:212px;height:210px;background:linear-gradient(150deg,#8e8178,#4d4a48)}
.doc-text{position:absolute;left:262px;top:20px;width:440px;font-size:9.5px;color:var(--muted)}
.doc-name{position:absolute;left:262px;top:244px;font-family:"Raleway",Arial,sans-serif;font-size:18px;color:var(--ink)}
.doc-more{position:absolute;left:620px;top:244px;font-size:9px;padding:5px 12px}
.consult{position:absolute;left:748px;top:10px;width:184px;height:300px;background:#f7f7f7;border:1px solid var(--line);padding:14px}
.consult h3{font-family:"Raleway",Arial,sans-serif;font-weight:400;font-size:10px;color:var(--muted);text-transform:uppercase;text-align:center;line-height:1.2}
.consult h3 b{display:block;font-size:17px;color:var(--ink);font-weight:400}
.field{height:20px;border:1px solid var(--line);background:var(--white);margin-top:7px;font-size:8.5px;color:#999;padding:3px 6px}
.field.tall{height:52px}
.consult .agree{font-size:8px;color:var(--muted);margin-top:8px;display:flex;gap:4px;align-items:center}
.consult .agree i{width:8px;height:8px;border:1px solid #aaa;display:block}
.consult .btn{font-size:9px;padding:4px 10px;margin-top:6px}

/* gallery */
.gallery{top:1620px;height:540px;background:linear-gradient(180deg,#3a3a3a,#222)}
.gallery h2{position:absolute;left:0;top:40px;color:var(--white)}
.gallery .view-all{position:absolute;right:0;top:44px;font-size:9px;padding:6px 12px}
.ba-row{position:absolute;left:0;top:184px;display:flex;gap:14px}
.ba{width:209px}
.ba .ph{width:209px;height:200px;background:linear-gradient(90deg,#c9a795 0 49.5%,#2e2e2e 49.5% 50.5%,#b8927e 50.5%)}
.ba .label{background:var(--accent);color:var(--white);font-size:11px;font-weight:600;padding:6px 10px;margin-top:0}

/* staff */
.staff{top:2160px;height:410px;background:var(--light)}
.staff h2{position:absolute;left:0;top:24px}
.staff .arrows{position:absolute;right:0;top:28px;display:flex;gap:4px}
.staff .arrows span{width:22px;height:22px;background:var(--accent);display:flex;align-items:center;justify-content:center}
.staff-row{position:absolute;left:0;top:120px;display:flex;gap:40px}
.member{width:190px;text-align:center}
.member .ph{width:150px;height:150px;border-radius:50%;background:linear-gradient(150deg,#d8d8d8,#9f9f9f);margin:0 auto 12px;border:4px solid var(--white)}
.member h3{font-family:"Raleway",Arial,sans-serif;font-weight:600;font-size:14px}
.member .role{font-size:9px;color:var(--muted);margin-bottom:4px}
.member p{font-size:9px;color:var(--muted);line-height:1.45}

/* media */
.media{top:2570px;height:330px}
.media h2{position:absolute;top:30px}
.media .videos-title{left:0}
.media .view-btn{position:absolute;left:324px;top:32px;font-size:9px;padding:5px 10px}
.video{position:absolute;left:0;top:82px;width:412px;height:220px;background:#111}
.video .ph{position:absolute;left:0;top:0;width:412px;height:196px;background:linear-gradient(135deg,#c4c4c4,#7a7a7a)}
.video .play{position:absolute;left:176px;top:70px}
.video .bar{position:absolute;left:0;bottom:0;width:412px;height:24px;background:#1a1a1a;display:flex;align-items:center;gap:8px;padding:0 8px}
.video .bar i{flex:1;height:4px;background:#555;position:relative;display:block}
.video .bar i::before{content:"";position:absolute;left:0;top:0;width:30%;height:4px;background:var(--accent)}
.media .test-title{left:440px}
.testimonial{position:absolute;left:440px;width:440px;background:var(--light);padding:12px 16px;font-size:9.5px;color:var(--muted)}
.testimonial b{display:block;color:var(--accent);font-weight:600;margin-top:4px}
.testimonial small{display:block;color:var(--accent);font-size:8.5px}

/* affiliates */
.affiliates{top:2900px;height:270px;background:#ececec}
.affiliates h2{position:absolute;left:0;top:30px}
.aff-row{position:absolute;left:20px;top:128px;display:flex;gap:62px;align-items:center}
.aff-row span{display:block;background:#c9c9c9}

/* footer */
.footer{top:3170px;height:342px;background:var(--dark);color:#aaa}
.foot-cols{position:absolute;left:0;top:40px;display:flex;gap:30px}
.foot-col{width:198px;font-size:9px;line-height:1.6}
.foot-col h4{font-family:"Raleway",Arial,sans-serif;font-weight:400;font-size:16px;color:var(--white);margin-bottom:12px}
.foot-col ul{list-style:none}
.foot-col li::before{content:"› ";color:var(--accent)}
.foot-col .group{color:var(--white);margin-top:6px}
.foot-col .two{display:flex;gap:20px}
.foot-col .input{height:20px;background:#444;margin:8px 0;color:#888;padding:3px 6px}
.foot-col .btn{font-size:9px;padding:4px 10px}
.foot-col .loc{color:var(--white);font-weight:600;margin-top:6px}
.bottom-bar{top:3512px;height:36px;background:var(--darker);color:#888;font-size:8.5px}
.bottom-bar .wrap{display:flex;justify-content:space-between;align-items:center}
</style>
</head>
<body>

<header class="section site-header">
  <div class="wrap">
    <div class="brand"><span class="brand-mark"></span><span class="brand-name">Harbourline Cosmetic Institute</span></div>
    <a class="btn top-cta">BOOK AN APPOINTMENT ONLINE</a>
    <div class="top-phone">
      <svg width="14" height="14" viewBox="0 0 24 24"><path fill="#29a9dc" d="M6.6 10.8c1.4 2.8 3.8 5.1 6.6 6.6l2.2-2.2c.3-.3.7-.4 1-.2 1.1.4 2.3.6 3.6.6.6 0 1 .4 1 1V20c0 .6-.4 1-1 1C10.6 21 3 13.4 3 4c0-.6.4-1 1-1h3.5c.6 0 1 .4 1 1 0 1.3.2 2.5.6 3.6.1.3 0 .7-.2 1l-2.3 2.2z"/></svg>
      +61 (02) 9000 4821
    </div>
    <div class="socials"><span></span><span></span><span></span><span></span></div>
    <nav class="nav">
      <span class="active">Home</span><span>About Us</span><span>Procedures</span><span>News</span><span>Patient Resources</span><span>Contact Us</span>
    </nav>
    <div class="search">Search here
      <svg width="12" height="12" viewBox="0 0 24 24"><circle cx="10" cy="10" r="6" fill="none" stroke="#999" stroke-width="2.5"/><path d="M15 15l6 6" stroke="#999" stroke-width="2.5"/></svg>
    </div>
  </div>
</header>

<section class="section hero">
  <div class="hero-side" style="left:0;width:156px"></div>
  <div class="hero-side" style="left:1044px;width:156px;background:linear-gradient(90deg,#9a9a9a,#cfcfcf)"></div>
  <div class="hero-main ph" role="img" aria-label="Hero photograph of a woman with soft natural skin">
    <div class="hero-copy">
      <h1>Nurture your natural beauty with the rejuvenation you deserve</h1>
      <a class="btn">View Our Procedures</a>
    </div>
  </div>
  <div class="hero-next">INVE<small>your</small></div>
</section>

<section class="section procedures">
  <div class="wrap">
    <h2 class="sec-title">Our Procedures</h2>
    <div class="proc-cards">
      <div class="proc-card"><div class="ph" role="img" aria-label="Body procedures photograph"></div><h3>Body</h3><p>Sculpt and refine your shape with tailored body contouring treatments.</p><span class="readmore">Read more</span></div>
      <div class="proc-card"><div class="ph" role="img" aria-label="Breast procedures photograph"></div><h3>Breast</h3><p>Augmentation, lift and reduction options planned around your goals.</p><span class="readmore">Read more</span></div>
      <div class="proc-card"><div class="ph" role="img" aria-label="Face procedures photograph"></div><h3>Facial</h3><p>Restore balance and freshness with gentle facial rejuvenation care.</p><span class="readmore">Read more</span></div>
      <div class="proc-card"><div class="ph" role="img" aria-label="Non surgical treatments photograph"></div><h3>Non Surgical</h3><p>Injectables and skin treatments with little or no recovery time.</p><span class="readmore">Read more</span></div>
    </div>
  </div>
</section>

<section class="section institute">
  <div class="wrap">
    <h2>Harbourline Cosmetic Institute</h2>
    <div class="sub">Your future looks beautiful</div>
    <p>You can expect natural results at the Harbourline Cosmetic Institute. With long experience in facial, breast and body surgery, our team takes time to understand your concerns and explain every option clearly before any treatment begins. We combine modern techniques with careful planning, so that each procedure suits your features, your lifestyle and your expectations. From the first consultation to the final review, our nurses and surgeons support you with honest advice, clear pricing and attentive aftercare. Our goal is simple: to help you feel confident, comfortable and at ease with the way you look, in a private and welcoming clinic setting.</p>
    <div class="center"><a class="btn">Enquire Now</a></div>
  </div>
</section>

<section class="section doctor">
  <div class="wrap">
    <h2 class="sec-title">Meet Dr Martin Ashcombe</h2>
    <div class="doc-box">
      <div class="doc-photo ph" role="img" aria-label="Portrait photograph of the surgeon"></div>
      <div class="doc-text">I decided that plastic surgery would be my calling early in my training. Over many years I have worked with patients from all walks of life, and I still believe that the best results come from listening carefully and planning every detail. I trained in reconstructive and cosmetic surgery in Australia and abroad, and I continue to learn from colleagues through teaching and research. My approach is conservative and natural, aiming for outcomes that look like you at your best rather than someone else. I enjoy helping patients regain confidence, and I am proud of the caring team that supports them before and after surgery.</div>
      <div class="doc-name">Dr Martin Ashcombe</div>
      <a class="btn doc-more">Read More</a>
      <div class="consult">
        <h3>Request your<b>Consultation</b></h3>
        <div class="field">First name</div>
        <div class="field">Email</div>
        <div class="field">Phone number</div>
        <div class="field">Procedure of interest</div>
        <div class="field tall">Message</div>
        <div class="agree"><i></i>I agree to the privacy terms</div>
        <a class="btn">Submit</a>
      </div>
    </div>
  </div>
</section>

<section class="section gallery">
  <div class="wrap">
    <h2 class="sec-title">Gallery Before / After</h2>
    <a class="btn view-all">VIEW FULL GALLERY</a>
    <div class="ba-row">
      <div class="ba"><div class="ph" role="img" aria-label="Before and after photographs of eyelid surgery"></div><div class="label">Blepharoplasty (Face)</div></div>
      <div class="ba"><div class="ph" role="img" aria-label="Before and after photographs of nose surgery"></div><div class="label">Rhinoplasty (Nose)</div></div>
      <div class="ba"><div class="ph" role="img" aria-label="Before and after photographs of tummy tuck surgery"></div><div class="label">Abdominoplasty (Tummy)</div></div>
      <div class="ba"><div class="ph" role="img" aria-label="Before and after photographs of body contouring"></div></div>
    </div>
  </div>
</section>

<section class="section staff">
  <div class="wrap">
    <h2 class="sec-title">Our Staff</h2>
    <div class="arrows">
      <span><svg width="10" height="10" viewBox="0 0 10 10"><path d="M7 1L3 5l4 4" fill="none" stroke="#fff" stroke-width="2"/></svg></span>
      <span><svg width="10" height="10" viewBox="0 0 10 10"><path d="M3 1l4 4-4 4" fill="none" stroke="#fff" stroke-width="2"/></svg></span>
    </div>
    <div class="staff-row">
      <div class="member"><div class="ph" role="img" aria-label="Staff portrait"></div><h3>Tessa Varden</h3><div class="role">Practice Manager</div><p>Tessa oversees the clinic and makes sure every patient visit runs smoothly.</p><span class="readmore">Read more</span></div>
      <div class="member"><div class="ph" role="img" aria-label="Staff portrait"></div><h3>Nina Holloway</h3><div class="role">Patient Coordinator</div><p>Nina guides patients through bookings, quotes and surgery planning.</p><span class="readmore">Read more</span></div>
      <div class="member"><div class="ph" role="img" aria-label="Staff portrait"></div><h3>Ruth Ashcombe</h3><div class="role">Clinic Director</div><p>Ruth manages the team and keeps the highest standards of patient care.</p><span class="readmore">Read more</span></div>
      <div class="member"><div class="ph" role="img" aria-label="Staff portrait"></div><h3>Maya Penrith</h3><div class="role">Registered Nurse</div><p>Maya supports patients before and after surgery with gentle aftercare.</p><span class="readmore">Read more</span></div>
    </div>
  </div>
</section>

<section class="section media">
  <div class="wrap">
    <h2 class="sec-title videos-title">Instructional Videos</h2>
    <a class="btn view-btn">View all videos</a>
    <div class="video">
      <div class="ph" role="img" aria-label="Video still of a patient consultation"></div>
      <svg class="play" width="60" height="42" viewBox="0 0 60 42"><rect width="60" height="42" rx="10" fill="#cc2b2b"/><path d="M24 12l14 9-14 9z" fill="#fff"/></svg>
      <div class="bar">
        <svg width="10" height="10" viewBox="0 0 10 10"><path d="M1 0l8 5-8 5z" fill="#ddd"/></svg>
        <i></i>
        <span style="color:#aaa;font-size:8px">0:00 / 3:42</span>
      </div>
    </div>
    <h2 class="sec-title test-title">Testimonials</h2>
    <div class="testimonial" style="top:82px">"From the first visit I felt listened to and cared for. The team explained everything and my recovery was easier than I expected. I am delighted with my natural result and would happily recommend the clinic."<b>Sarah K.</b><small>Breast Augmentation</small></div>
    <div class="testimonial" style="top:196px">"Professional, warm and honest advice from start to finish. The nurses checked in often and I always knew what to expect. Thank you for helping me feel like myself again."<b>Louise M.</b><small>Facial Rejuvenation</small></div>
  </div>
</section>

<section class="section affiliates">
  <div class="wrap">
    <h2 class="sec-title">Our Affiliates</h2>
    <div class="aff-row">
      <span style="width:80px;height:40px"></span>
      <span style="width:70px;height:70px;border-radius:50%"></span>
      <span style="width:70px;height:70px;border-radius:50%"></span>
      <span style="width:90px;height:34px"></span>
      <span style="width:100px;height:46px;border-radius:23px"></span>
      <span style="width:70px;height:50px"></span>
    </div>
  </div>
</section>

<footer class="section footer">
  <div class="wrap">
    <div class="foot-cols">
      <div class="foot-col">
        <h4>About us</h4>
        <p>We are a dedicated team of surgeons and nurses offering safe, natural cosmetic care in a private clinic, with clear advice and support at every step.</p>
        <ul style="margin-top:10px"><li>Our Surgeon</li><li>Meet the Team</li></ul>
      </div>
      <div class="foot-col">
        <h4>Surgical Procedures</h4>
        <div class="two">
          <ul><li class="group">Face</li><li>Facelift</li><li>Eyelid Surgery</li><li>Nose Surgery</li><li class="group">Body</li><li>Tummy Tuck</li><li>Liposuction</li></ul>
          <ul><li class="group">Breast</li><li>Augmentation</li><li>Breast Lift</li><li>Reduction</li><li class="group">Other</li><li>Injectables</li><li>Skin Care</li></ul>
        </div>
      </div>
      <div class="foot-col">
        <h4>Newsletter</h4>
        <p>Subscribe to our newsletter for news, offers and updates.</p>
        <div class="input">Enter email address</div>
        <a class="btn">Subscribe</a>
      </div>
      <div class="foot-col">
        <h4>Our Clinics</h4>
        <div class="loc">City Clinic</div><p>Level 4, 120 Harbour Street<br>Sydney NSW 2000</p>
        <div class="loc">North Shore</div><p>18 Ridge Road<br>Chatswood NSW 2067</p>
        <p style="margin-top:6px">T: +61 (02) 9000 4821<br>info@harbourlinecosmetic.org</p>
      </div>
    </div>
  </div>
</footer>

<div class="section bottom-bar">
  <div class="wrap"><span>© 2016 Harbourline Cosmetic Institute. All rights reserved.</span><span>Home | Privacy | Terms | Contact</span></div>
</div>

</body>
</html>
```